Tallow & Mersey Needs New Stationery / Letterhead Design

We need new stationery to match our new logo (attached). Tallow & Mersey is a 34 year old nationwide law firm located in Houston Tx. They do personal injury law and pharmaceutical litigation.

WE DO NOT NEED BUSINESS CARDS.

Attached are several different file formats of the new logo.

Reason: We will make a decision in the next couple days. Finalizing edits now. Thank you!

Target Market(s)

consumers who have been injured due to the negligence of another or by a pharmaceutical drug or defective medical device. Also co-counsel and opposing counsel (law firms0.

Industry/Entity Type

Law Firm

Requirements
Must have
• logo
• Tallow & Mersey, LLP
• 7183 Corvid Lane, Suite 1000
• Brenford, TX 75591
• Tel: (555) 408-1936
• Fax: (555) 408-2275
• www.tallowandmersey.example
• Must have colors in the logo.
• Make the font go with the logo - not necessarily the same, but something that goes well with it.

```html
<!DOCTYPE html>
<html lang="en">
<head>
<meta charset="utf-8">
<title>Tallow &amp; Mersey Stationery</title>
<link href="https://fonts.googleapis.com/css2?family=Montserrat:wght@400;600&display=swap" rel="stylesheet">
<style>
  :root {
    --navy: #2c3e63;
    --charcoal: #3a3a3a;
    --paper: #f4f4f4;
    --ink: #3c3c3c;
    --backdrop: #d4d4d4;
    --on-navy: #ffffff;
  }
  * { margin: 0; padding: 0; box-sizing: border-box; }
  html, body { width: 1200px; height: 1000px; overflow: hidden; }
  body { background: var(--backdrop); position: relative; font-family: "Montserrat", sans-serif; color: var(--ink); }

  .sheet { position: absolute; }
  .wordmark { font-family: "Montserrat", sans-serif; font-weight: 600; line-height: 1; letter-spacing: 0.01em; white-space: nowrap; }
  .tagline { font-size: 4.6px; letter-spacing: 0.14em; text-transform: uppercase; white-space: nowrap; margin-top: 4px; }
  .footer-band { position: absolute; left: 0; bottom: 0; display: block; }

  /* Presentation folder */
  .folder { left: 122px; top: 70px; width: 460px; height: 596px; background: var(--navy); border-radius: 4px; }
  .folder-spine { position: absolute; left: 28px; top: 0; bottom: 0; width: 2px; background: rgba(0,0,0,0.18); }
  .folder-brand { position: absolute; left: 0; right: 0; top: 150px; text-align: center; color: var(--on-navy); }
  .folder-brand .mark { width: 18px; height: 18px; background: var(--on-navy); margin: 0 auto 14px; }
  .folder-brand .wordmark { font-size: 20px; }
  .folder-brand .tagline { font-size: 6.5px; margin-top: 6px; }
  .folder-url { position: absolute; left: 0; right: 0; top: 550px; text-align: center; color: var(--on-navy); font-size: 8.5px; }

  /* Letterhead */
  .letterhead { left: 617px; top: 91px; width: 445px; height: 575px; background: var(--paper); }
  .lh-brand { position: absolute; left: 36px; top: 30px; color: var(--navy); }
  .lh-brand .mark { width: 12px; height: 12px; background: var(--navy); margin-bottom: 8px; }
  .lh-brand .wordmark { font-size: 12px; }
  .lh-contact { position: absolute; left: 319px; top: 32px; font-size: 5px; line-height: 1.55; }
  .lh-contact li { list-style: none; display: flex; align-items: center; gap: 3px; }
  .lh-contact .icon { width: 5px; height: 5px; background: var(--navy); border-radius: 1px; }
  .lh-contact address { font-style: normal; margin-top: 4px; }
  .letter { position: absolute; left: 36px; top: 129px; width: 373px; font-size: 5.4px; line-height: 1.45; }
  .letter .date { margin-bottom: 9px; }
  .letter .recipient { font-style: normal; margin-bottom: 25px; }
  .letter .salutation { font-weight: 600; margin-bottom: 8px; }
  .letter p { text-align: justify; margin-bottom: 7px; }
  .letter .closing { margin-top: 12px; position: relative; }
  .letter .closing strong { font-weight: 600; display: block; }
  .signature { position: absolute; left: 52px; top: -8px; width: 96px; height: 36px; background: linear-gradient(90deg, rgba(70,100,190,0.12), rgba(70,100,190,0.05)); border-radius: 3px; }

  /* Envelope front */
  .envelope-front { left: 84px; top: 698px; width: 497px; height: 216px; background: var(--paper); }
  .ef-brand { position: absolute; left: 28px; top: 22px; color: var(--navy); }
  .ef-brand .mark { width: 12px; height: 12px; background: var(--navy); margin-bottom: 8px; }
  .ef-brand .wordmark { font-size: 12px; }
  .ef-address { position: absolute; left: 46px; top: 182px; font-style: normal; font-size: 5.4px; line-height: 1.4; text-align: center; }

  /* Envelope back */
  .envelope-back { left: 617px; top: 698px; width: 497px; height: 216px; background: var(--paper); }
  .eb-flap { position: absolute; left: 0; top: 0; display: block; }
  .eb-brand { position: absolute; left: 0; right: 0; top: 30px; text-align: center; color: var(--on-navy); }
  .eb-brand .wordmark { font-size: 9px; }
  .eb-brand .tagline { font-size: 3.8px; margin-top: 3px; }
  .eb-url { position: absolute; left: 0; right: 0; top: 188px; text-align: center; font-size: 5.4px; color: var(--navy); }
</style>
</head>
<body>

<section class="sheet folder" aria-label="Presentation folder">
  <div class="folder-spine"></div>
  <div class="folder-brand">
    <div class="mark"></div>
    <div class="wordmark">Tallow &amp; Mersey</div>
    <div class="tagline">Personal Injury &amp; Drug Litigation</div>
  </div>
  <div class="folder-url">www.tallowandmersey.example</div>
</section>

<section class="sheet letterhead" aria-label="Letterhead">
  <div class="lh-brand">
    <div class="mark"></div>
    <div class="wordmark">Tallow &amp; Mersey</div>
    <div class="tagline">Personal Injury &amp; Drug Litigation</div>
  </div>
  <div class="lh-contact">
    <ul>
      <li><span class="icon"></span>(555) 408-1936</li>
      <li><span class="icon"></span>(555) 408-2275</li>
      <li><span class="icon"></span>www.tallowandmersey.example</li>
    </ul>
    <address>7183 Corvid Lane, Suite 1000<br>Brenford, TX 75591</address>
  </div>
  <div class="letter">
    <div class="date">30.11.2016</div>
    <address class="recipient">Recipient's name<br>Lindenweg 12<br>40210 Halverstadt<br>Germany</address>
    <div class="salutation">Dear sir,</div>
    <p>Communication is a very integral part of living creatures, animals and humans. Communication may be verbal or written. Written communication however is only applicable to human beings. Can you even imagine a world without communication? Verbal communication can be through telephones, webcams or in person. Written communication is through letters, emails and mobile phone messages.</p>
    <p>In today's world of great inventions and technology, letters have somehow become redundant. It is the time for text messages or chats. But they still can communicate a lot more than all other modes of communication. Organizations and various government departments still bank on letters as a strong medium of communication. There is no comparison in costs of sending letters as compared to costs of mobile phone messages though – letters are far cheaper. Letters now commonly known as "hard copy documents" are considered more relevant and important than email copies of text messages as proof or evidence of some sort.</p>
    <p>Letters speak volumes about a person or an organization that writes it. So one must take utmost care ensuring that the language used in any letter is appropriate for the occasion for which it is being written. Since a letter is also a written proof or document, if there are certain things that should not form a part of it, then that too should be carefully handled.</p>
    <p>Writing a good letter is an art. But if for some reason someone is unable to write that perfect letter, these different types of letters provide a base for you to build on. Sample letters have been given for everyone to understand what all information needs to form a part of the letter type and then it can be customized.</p>
    <div class="closing">Yours Sincerely,<strong>Dana Whitlow</strong>
      <div class="signature" role="img" aria-label="Handwritten signature in blue ink"></div>
    </div>
  </div>
  <svg class="footer-band" width="445" height="8" viewBox="0 0 445 8" aria-hidden="true">
    <rect x="0" y="2" width="292" height="6" fill="var(--charcoal)"/>
    <polygon points="296,8 303,0 445,0 445,8" fill="var(--navy)"/>
  </svg>
</section>

<section class="sheet envelope-front" aria-label="Envelope front">
  <div class="ef-brand">
    <div class="mark"></div>
    <div class="wordmark">Tallow &amp; Mersey</div>
    <div class="tagline">Personal Injury &amp; Drug Litigation</div>
  </div>
  <address class="ef-address">7183 Corvid Lane, Suite 1000<br>Brenford, TX 75591</address>
  <svg class="footer-band" width="497" height="8" viewBox="0 0 497 8" aria-hidden="true">
    <rect x="0" y="2" width="346" height="6" fill="var(--charcoal)"/>
    <polygon points="350,8 357,0 497,0 497,8" fill="var(--navy)"/>
  </svg>
</section>

<section class="sheet envelope-back" aria-label="Envelope back">
  <svg class="eb-flap" width="497" height="70" viewBox="0 0 497 70" aria-hidden="true">
    <polygon points="0,0 497,0 479,68 19,68" fill="var(--navy)"/>
  </svg>
  <div class="eb-brand">
    <div class="wordmark">Tallow &amp; Mersey</div>
    <div class="tagline">Personal Injury &amp; Drug Litigation</div>
  </div>
  <div class="eb-url">www.tallowandmersey.example</div>
</section>

</body>
</html>
```